Business Card Design Project

we need a business card design for our company: www.plomvik.ch
It's important to include our already existing logo (see website)

```html
<!DOCTYPE html>
<html lang="de">
<head>
<meta charset="utf-8">
<title>Plomvik – Visitenkarte</title>
<link rel="stylesheet" href="https://fonts.googleapis.com/css2?family=Arimo:wght@400;700&display=swap">
<style>
  :root {
    --page: #ffffff;
    --card: #e8e8e8;
    --card-edge: #d2d2d2;
    --brand-blue: #2196f3;
    --logo-blue: #4aa6f2;
    --ink: #111111;
    --band-text: #eaf4ff;
  }
  * { box-sizing: border-box; margin: 0; padding: 0; }
  html, body {
    width: 1200px;
    height: 356px;
    overflow: hidden;
    background: var(--page);
    font-family: "Arimo", Arial, sans-serif;
  }
  .sheet {
    position: relative;
    width: 1200px;
    height: 356px;
  }
  .card {
    position: absolute;
    top: 27px;
    width: 584px;
    height: 326px;
    background: linear-gradient(180deg, #ececec 0%, var(--card) 100%);
    border: 1px solid var(--card-edge);
    border-radius: 22px;
    overflow: hidden;
    box-shadow: 0 1px 3px rgba(0,0,0,0.12);
  }
  .card--front { left: 4px; }
  .card--back { left: 612px; }

  .band {
    position: absolute;
    left: 0;
    bottom: 0;
    width: 100%;
    height: 100px;
    display: block;
  }
  .band path { fill: var(--brand-blue); }

  .web-address {
    position: absolute;
    left: 0;
    right: 0;
    bottom: 14px;
    text-align: center;
    color: var(--band-text);
    font-size: 20px;
    letter-spacing: 0.55em;
    padding-left: 0.55em;
  }

  .brand-name {
    color: var(--logo-blue);
    font-weight: 700;
    letter-spacing: -0.01em;
  }
  .card--front .brand-name {
    position: absolute;
    left: 0;
    right: 0;
    top: 100px;
    text-align: center;
    font-size: 68px;
    line-height: 1;
  }
  .card--back .brand-name {
    position: absolute;
    left: 30px;
    top: 26px;
    font-size: 22px;
    line-height: 1;
  }

  .holder {
    position: absolute;
    left: 77px;
    top: 71px;
    color: var(--ink);
  }
  .holder-name {
    font-size: 26px;
    font-weight: 700;
    line-height: 1.1;
  }
  .holder-role {
    font-size: 15px;
    margin-top: 2px;
  }

  .contact {
    position: absolute;
    left: 82px;
    top: 144px;
    list-style: none;
    color: var(--ink);
    font-size: 16px;
  }
  .contact li {
    display: flex;
    align-items: center;
    height: 20px;
  }
  .contact svg {
    width: 18px;
    height: 16px;
    margin-right: 8px;
    fill: var(--brand-blue);
    flex: none;
  }
</style>
</head>
<body>
<main class="sheet">
  <section class="card card--front" aria-label="Vorderseite">
    <div class="brand-name">Plomvik</div>
    <svg class="band" viewBox="0 0 584 100" preserveAspectRatio="none" aria-hidden="true">
      <path d="M0 0 H252 V6 A40 40 0 0 0 332 6 V0 H584 V100 H0 Z"/>
    </svg>
    <div class="web-address">www.plomvik.ch</div>
  </section>

  <section class="card card--back" aria-label="Rückseite">
    <div class="brand-name">Plomvik</div>
    <div class="holder">
      <h1 class="holder-name">Mk. Lars Fenner</h1>
      <p class="holder-role">Software Engineer</p>
    </div>
    <ul class="contact">
      <li>
        <svg viewBox="0 0 18 16" aria-hidden="true"><path d="M9 1 L17 8 H14.5 V15 H10.5 V10.5 H7.5 V15 H3.5 V8 H1 Z"/></svg>
        AG - Talackerweg 12 - 8052
      </li>
      <li>
        <svg viewBox="0 0 18 16" aria-hidden="true"><path d="M4 1.5 C5 1 6 1.2 6.6 2.4 L7.6 4.6 C8 5.4 7.7 6.1 7 6.6 L6.3 7.1 C7 8.9 8.3 10.3 10.1 11.1 L10.7 10.3 C11.2 9.7 11.9 9.5 12.7 9.9 L14.8 11 C15.9 11.6 16 12.6 15.5 13.5 C14.7 14.8 13.2 15.3 11.6 14.7 C7.5 13.3 4.2 10 2.6 5.8 C2 4.2 2.6 2.4 4 1.5 Z"/></svg>
        Telefon: 044 613 47 90
      </li>
      <li>
        <svg viewBox="0 0 18 16" aria-hidden="true"><path d="M1 3 H17 V13 H1 Z M2.2 4 L9 9 L15.8 4 Z" fill-rule="evenodd"/></svg>
        Mail: info@plomvik.ch
      </li>
    </ul>
    <svg class="band" viewBox="0 0 584 100" preserveAspectRatio="none" aria-hidden="true">
      <path d="M0 0 H252 V6 A40 40 0 0 0 332 6 V0 H584 V100 H0 Z"/>
    </svg>
    <div class="web-address">www.plomvik.ch</div>
  </section>
</main>
</body>
</html>
```